Brennick Holdings Business Cards

These are professional business cards that are for my family office.
Put fake emails and phone numbers as of now until I finalize those components. This family office controls my families investments, assets, and future. The cards should be professional.
..
.
.
.
I just uploaded another variation of a logo I would like to see as a business card to I am inbeteen which logo to use

Target Market(s)

business

Industry/Entity Type

business

Contact Information for Business Card

Professional, wealth related, finance related.

Requirements
Must have
• Logo

```html
<!DOCTYPE html>
<html lang="en">
<head>
<meta charset="utf-8">
<title>Brennick Holdings Business Cards</title>
<link href="https://fonts.googleapis.com/css2?family=Poppins:wght@400;500;600;700&display=swap" rel="stylesheet">
<style>
  :root {
    --backdrop: #e2e6e7;
    --card: #ffffff;
    --ink: #161c2a;
    --muted: #9b9b9b;
    --rule: #6a6d74;
  }
  * { margin: 0; padding: 0; box-sizing: border-box; }
  html, body {
    width: 1200px; height: 960px; overflow: hidden;
    background: var(--backdrop);
    font-family: "Poppins", sans-serif;
    color: var(--ink);
  }
  .canvas { position: relative; width: 1200px; height: 960px; }
  .card {
    position: absolute; left: 250px; width: 701px; height: 400px;
    background: var(--card);
    box-shadow: 0 14px 22px rgba(0,0,0,0.28);
  }
  .card--front { top: 60px; }
  .card--back { top: 500px; }
  .side-bar {
    position: absolute; top: 100px; width: 16px; height: 200px;
    background: var(--ink);
  }
  .side-bar--left { left: 0; }
  .side-bar--right { right: 0; }

  .brand {
    position: absolute; display: flex; flex-direction: column; align-items: center;
    transform: translateX(-50%);
  }
  .brand__dot { border-radius: 50%; background: var(--ink); }
  .brand__name { font-weight: 600; white-space: nowrap; letter-spacing: 0.5px; }

  .card--front .brand { left: 350px; top: 150px; }
  .card--front .brand__dot { width: 18px; height: 18px; margin-bottom: 22px; }
  .card--front .brand__name { font-size: 38px; line-height: 1; }

  .card--back .brand { left: 165px; top: 168px; }
  .card--back .brand__dot { width: 12px; height: 12px; margin-bottom: 14px; }
  .card--back .brand__name { font-size: 21px; line-height: 1; }

  .divider {
    position: absolute; left: 350px; top: 81px; width: 1px; height: 240px;
    background: var(--rule);
  }
  .person { position: absolute; left: 405px; top: 116px; }
  .person__name { font-size: 31px; line-height: 1.1; font-weight: 400; letter-spacing: 0.3px; }
  .person__name strong { font-weight: 700; }
  .person__title { font-size: 15.5px; font-weight: 600; margin-top: 2px; letter-spacing: 0.3px; }

  .contacts { position: absolute; left: 405px; top: 199px; list-style: none; }
  .contacts li {
    display: flex; align-items: center; height: 26px;
    font-size: 17.5px; letter-spacing: 0.4px;
  }
  .contacts svg { width: 17px; height: 17px; margin-right: 11px; fill: var(--ink); flex: none; }

  .address {
    position: absolute; left: 0; right: 0; top: 343px;
    text-align: center; font-size: 16.5px; font-weight: 500; letter-spacing: 0.3px;
  }
</style>
</head>
<body>
<main class="canvas">
  <section class="card card--front">
    <div class="side-bar side-bar--left"></div>
    <div class="side-bar side-bar--right"></div>
    <div class="brand">
      <span class="brand__dot"></span>
      <span class="brand__name">Brennick Holdings</span>
    </div>
  </section>

  <section class="card card--back">
    <div class="side-bar side-bar--left"></div>
    <div class="side-bar side-bar--right"></div>
    <div class="brand">
      <span class="brand__dot"></span>
      <span class="brand__name">Brennick Holdings</span>
    </div>
    <div class="divider"></div>
    <div class="person">
      <h1 class="person__name"><strong>Marta</strong> Kovalen</h1>
      <p class="person__title">Founder &amp; CEO</p>
    </div>
    <ul class="contacts">
      <li>
        <svg viewBox="0 0 24 24" aria-hidden="true"><path d="M6.6 10.8a15.1 15.1 0 0 0 6.6 6.6l2.2-2.2a1 1 0 0 1 1-.25 11.4 11.4 0 0 0 3.6.57 1 1 0 0 1 1 1V20a1 1 0 0 1-1 1A17 17 0 0 1 3 4a1 1 0 0 1 1-1h3.5a1 1 0 0 1 1 1c0 1.25.2 2.45.57 3.57a1 1 0 0 1-.25 1z"/></svg>
        (555) 204-6188
      </li>
      <li>
        <svg viewBox="0 0 24 24" aria-hidden="true"><path d="M12 2a10 10 0 1 0 0 20 10 10 0 0 0 0-20zm6.9 6h-2.9a15.7 15.7 0 0 0-1.4-3.6A8 8 0 0 1 18.9 8zM12 4c.8 1.2 1.5 2.5 1.9 4h-3.8c.4-1.5 1.1-2.8 1.9-4zM4.3 14a8 8 0 0 1 0-4h3.4a16 16 0 0 0 0 4zm.8 2h2.9c.3 1.3.8 2.5 1.4 3.6A8 8 0 0 1 5.1 16zM8 8H5.1a8 8 0 0 1 4.3-3.6C8.8 5.5 8.3 6.7 8 8zm4 12c-.8-1.2-1.5-2.5-1.9-4h3.8c-.4 1.5-1.1 2.8-1.9 4zm2.3-6H9.7a14.6 14.6 0 0 1 0-4h4.6a14.6 14.6 0 0 1 0 4zm.3 5.6c.6-1.1 1.1-2.3 1.4-3.6h2.9a8 8 0 0 1-4.3 3.6zm1.7-5.6a16 16 0 0 0 0-4h3.4a8 8 0 0 1 0 4z"/></svg>
        info@yourwebsite.com
      </li>
      <li>
        <svg viewBox="0 0 24 24" aria-hidden="true"><path d="M3 5h18a1 1 0 0 1 1 1v12a1 1 0 0 1-1 1H3a1 1 0 0 1-1-1V6a1 1 0 0 1 1-1zm9 7.5L4.5 7v10h15V7z"/></svg>
        www.yourwebsite.com
      </li>
    </ul>
    <p class="address">412 Harlow Ridge Dr Marston, Texas 75990 USA</p>
  </section>
</main>
</body>
</html>
```